Bold, Modern, Clean "Quarvenstretch.com" website

Why we stand out?
We are a male and female mobile massage team. Our names are Todd and Lise. 
Quarven Tide is a Seattle based mobile massage service. Our massage is offered to the community with a goal of facilitating balance within each individual. We specialize in integrated Pain management, and sports/medical massage therapy. Every client's first assessment is attended by our male and female massage therapist team. Depending on the goals identified for an individual determines which therapist will be assigned to provide treatment, if not both.

Our passion...
Here at Quarven Tide, we have a great passion for Postural Resoration and how it is integrated into an individual's Massage treatment. We pride ourselves in being natural facilitators of healing, which takes the ego of the therapist out of the client's healing process. We strive to deliver the best massage possible by including modalities such as Neuromuscular, Myofascial release, spontaneous muscle release, postural restoration, orthopedic, and medical massage.

Our education...

We are both Graduates of Halvenor, school of massage therapy. We have continuing education in medical massage, myofacial release, trigger point therapy, postural restoration, anatomy, and spontaneous muscle release. Lise is also a Certified Yoga Instructor, which amplifies her experience with flexibility and strength as it pertains to each individual. Todd's passion is Massage, stretching, and strength training to encourage postural restoration and realignment.

Our rates-

Our rates are $75/ 60 minutes, $95/ 90 minutes, and $120/ 120 minutes.

Education-
Both Lise and I worked as behavioral health professionals that specialized in life skills mentoring for youth who had experienced different types of trauma. This led us both to want to help others in a different environment, where individuals can be empowered to take responsibility over their own healing. To us, massage is a type of manipulation physical therapy, that encourages healing on many levels.

Advice to any massage client-
The most important thing to 'us', as Licenced providers is to get you on to our table to show you our skills. But a good therapist never forgets that it's not about what we do for you, but what we can facilitate for you. Your health and healing has nothing to do with us. It is yours, not ours. Identify what your goals are with any Therapist, and know what the end looks like. Progress should be tangible, such as range of motion, and decreased pain.

5/5 stars Massage Therapy
Verified Review

Lise and Todd at Quarven Tide are awesome! I recently had open heart surgery, and Lise worked on me to increase my range of motion while helping with the pinched nerve from my arm being in the same position for so long during my surgery. My wife drives a lot for work, and Todd has helped decrease her neck and lower back pain immensely. They are seriously the best therapists I have ever worked with. I would recommend them to anyone who needs anything from stress relief to a medical massage treatment. They are professional, up beat, easy going, and always on time. And, I love that they meet us where ever we like! We did a staycation recently, where they came to our hotel to give us relaxation massages. Although usually they come to our home, where we focus on pain related issues. We will continue to work with them for a long, long time.

Bressa K. on December 17, 2015

Target Market(s)

Mobile massage therapy clients

Industry/Entity Type

Massage Therapy

Font styles to use
Serif
Sans Serif

Requirements
Must have
• Please add or remove any information that would help the presentation of our website. Our logo is posted below, please include into the website.
• Please include a contact field that includes, quarvenstretch@mailbrook.net,
• (206) 555-0194
• We have also included our own stock photos, as well as a photo of Todd and Lise. Please include a cropped photo of both massage therapists.

```html
<!DOCTYPE html>
<html lang="en">
<head>
<meta charset="utf-8">
<title>Quarven Tide — Mobile Massage</title>
<link rel="stylesheet" href="https://fonts.googleapis.com/css2?family=Arvo:wght@400;700&family=Montserrat:wght@400;600&display=swap">
<style>
:root{
  --navy:#252a6b;
  --teal:#0399c6;
  --white:#ffffff;
  --bg-dark:#2e241f;
  --bg-mid:#5a4a40;
  --glow:0 0 18px rgba(255,255,255,.45);
}
*{box-sizing:border-box;margin:0;padding:0}
html,body{width:975px;height:1200px;overflow:hidden}
body{position:relative;font-family:"Arvo",Georgia,serif;color:var(--white);background:var(--bg-dark)}
.hero-photo{position:absolute;inset:0;background:radial-gradient(ellipse at 55% 42%,#7a6a5e 0%,var(--bg-mid) 35%,#3a2e28 70%,var(--bg-dark) 100%)}
.ring{position:absolute;border-radius:50%;background:var(--navy);border:solid var(--white);box-shadow:var(--glow)}
.ring--top{left:238px;top:-294px;width:498px;height:498px;border-width:34px}
.ring--bottom{left:238px;top:994px;width:498px;height:498px;border-width:34px}
.ring--left{left:-362px;top:304px;width:568px;height:568px;border-width:24px}
.ring--right{left:771px;top:300px;width:568px;height:568px;border-width:24px}
.nav-circle{position:absolute;width:204px;height:204px;border-radius:50%;background:var(--teal);border:14px solid var(--white);box-shadow:var(--glow)}
.nav-circle--home{left:45px;top:84px}
.nav-circle--education{left:730px;top:84px}
.nav-circle--testimonials{left:45px;top:892px}
.nav-circle--contact{left:730px;top:892px}
.petal{position:absolute;background:var(--teal);border:11px solid var(--white);box-shadow:var(--glow)}
.petal--why{left:240px;top:334px;width:232px;height:240px;border-radius:4px 120px 120px 120px}
.petal--passion{left:500px;top:334px;width:240px;height:240px;border-radius:120px 4px 120px 120px}
.petal--rates{left:253px;top:602px;width:239px;height:240px;border-radius:120px 120px 120px 4px}
.petal--stars{left:500px;top:612px;width:240px;height:240px;border-radius:120px 120px 4px 120px}
.label{position:absolute;transform:translateX(-50%);text-align:center;white-space:nowrap;text-transform:uppercase}
.label--nav{font-size:22px}
.label--nav-long{font-size:18px;letter-spacing:-.4px}
.label--petal{font-size:17px;line-height:22px}
.label--small{font-size:14px;line-height:18px;font-weight:700}
.icon{position:absolute;transform:translate(-50%,-50%)}
.brand{position:absolute;left:402px;top:1px;width:160px;height:160px;border-radius:50%;background:var(--teal);border:5px solid var(--white);display:flex;flex-direction:column;align-items:center;justify-content:center}
.brand__name{font-family:"Montserrat",Arial,sans-serif;font-weight:600;font-size:24px;line-height:25px;text-align:center;text-transform:uppercase}
.brand__tag{font-family:"Montserrat",Arial,sans-serif;font-size:11px;margin-top:6px}
.social{position:absolute;width:38px;height:36px;border:1px solid rgba(255,255,255,.8);font-family:"Montserrat",Arial,sans-serif;font-size:7px;display:flex;align-items:center;justify-content:center;text-transform:uppercase;letter-spacing:.3px}
.social--active{background:var(--white);color:var(--navy);width:38px;height:35px}
.contact-line{position:absolute;transform:translateX(-50%);text-align:center;white-space:nowrap}
.contact-line--call{left:891px;top:540px;font-size:18px;line-height:22px}
.contact-line--email{left:490px;top:1060px;font-size:15px;line-height:17px}
.copyright{position:absolute;left:490px;top:1156px;transform:translateX(-50%);font-family:"Montserrat",Arial,sans-serif;font-size:9px;white-space:nowrap}
</style>
</head>
<body>
<div class="hero-photo" role="img" aria-label="Softly blurred photo of a massage session in warm brown tones"></div>

<div class="ring ring--top"></div>
<div class="ring ring--bottom"></div>
<div class="ring ring--left"></div>
<div class="ring ring--right"></div>

<div class="brand">
  <span class="brand__name">Quarven<br>Tide</span>
  <span class="brand__tag">mobile massage</span>
</div>

<nav>
  <div class="nav-circle nav-circle--home"></div>
  <svg class="icon" style="left:143px;top:167px" width="34" height="28" viewBox="0 0 34 28" fill="#fff"><path d="M17 2 2 15h4v12h8v-8h6v8h8V15h4z"/></svg>
  <span class="label label--nav" style="left:146px;top:192px">Home</span>

  <div class="nav-circle nav-circle--education"></div>
  <svg class="icon" style="left:828px;top:167px" width="36" height="36" viewBox="0 0 36 36"><circle cx="18" cy="18" r="15" fill="none" stroke="#fff" stroke-width="6"/><circle cx="18" cy="18" r="7" fill="none" stroke="#0399c6" stroke-width="3"/><path d="M8 8l6 6M28 8l-6 6M8 28l6-6M28 28l-6-6" stroke="#0399c6" stroke-width="3"/></svg>
  <span class="label label--nav" style="left:835px;top:200px">Education</span>

  <div class="nav-circle nav-circle--testimonials"></div>
  <svg class="icon" style="left:147px;top:977px" width="38" height="30" viewBox="0 0 38 30"><rect x="2" y="2" width="34" height="26" rx="3" fill="none" stroke="#fff" stroke-width="3"/><path d="M3 4l16 13L35 4" fill="none" stroke="#fff" stroke-width="3"/></svg>
  <span class="label label--nav-long" style="left:147px;top:1004px">Testimonials</span>

  <div class="nav-circle nav-circle--contact"></div>
  <svg class="icon" style="left:832px;top:965px" width="24" height="32" viewBox="0 0 24 32" fill="#fff"><path d="M12 1C6 1 1 6 1 12c0 8 11 19 11 19s11-11 11-19C23 6 18 1 12 1zm0 15a4 4 0 1 1 0-8 4 4 0 0 1 0 8z"/></svg>
  <span class="label label--nav" style="left:834px;top:1006px">Contact Us</span>
</nav>

<section>
  <div class="petal petal--why"></div>
  <svg class="icon" style="left:349px;top:421px" width="36" height="36" viewBox="0 0 36 36"><circle cx="18" cy="18" r="15" fill="none" stroke="#fff" stroke-width="6"/><circle cx="18" cy="18" r="7" fill="none" stroke="#0399c6" stroke-width="3"/><path d="M8 8l6 6M28 8l-6 6M8 28l6-6M28 28l-6-6" stroke="#0399c6" stroke-width="3"/></svg>
  <span class="label label--petal" style="left:350px;top:472px">Why we stand<br>out?</span>

  <div class="petal petal--passion"></div>
  <svg class="icon" style="left:620px;top:424px" width="30" height="28" viewBox="0 0 30 28" fill="#fff"><path d="M15 27 3 15C-2 10 1 2 8 2c3 0 5 2 7 4 2-2 4-4 7-4 7 0 10 8 5 13z"/></svg>
  <span class="label label--petal" style="left:626px;top:468px">Our Passion</span>

  <div class="petal petal--rates"></div>
  <svg class="icon" style="left:364px;top:692px" width="30" height="38" viewBox="0 0 30 38"><rect x="1" y="1" width="28" height="36" rx="2" fill="#fff"/><g fill="#0399c6"><rect x="6" y="6" width="3" height="3"/><rect x="12" y="6" width="3" height="3"/><rect x="18" y="6" width="3" height="3"/><rect x="6" y="12" width="3" height="3"/><rect x="12" y="12" width="3" height="3"/><rect x="18" y="12" width="3" height="3"/><rect x="6" y="18" width="3" height="3"/><rect x="12" y="18" width="3" height="3"/><rect x="18" y="18" width="3" height="3"/><rect x="11" y="27" width="8" height="6"/></g></svg>
  <span class="label label--petal" style="left:370px;top:740px">Our Rates</span>

  <div class="petal petal--stars"></div>
  <svg class="icon" style="left:615px;top:692px" width="38" height="38" viewBox="0 0 38 38"><circle cx="19" cy="19" r="17" fill="#fff"/><path d="M19 12l6 4-2 7h-8l-2-7z" fill="#0399c6"/><path d="M19 12V4M25 16l8-3M23 23l5 7M15 23l-5 7M13 16l-8-3" stroke="#0399c6" stroke-width="2"/></svg>
  <span class="label label--small" style="left:626px;top:747px">5/5 Stars Massage<br>Therapy</span>
</section>

<aside>
  <div class="social" style="left:44px;top:489px">Video</div>
  <div class="social" style="left:44px;top:547px">Work</div>
  <div class="social social--active" style="left:100px;top:572px">Page</div>
  <div class="social" style="left:44px;top:605px">Posts</div>
  <div class="social" style="left:44px;top:663px">Photos</div>
</aside>

<footer>
  <p class="contact-line contact-line--call">Call Us<br>(206) 555-0194</p>
  <p class="contact-line contact-line--email">Email Address<br>quarvenstretch@mailbrook.net</p>
  <p class="copyright">Copyright 2015 Company Name. All Rights Reserved.</p>
</footer>
</body>
</html>
```